Marketing Flyer for Plumber Referals

8.5" x11" Layout should be landscape not portrait. Create a bold, eye-catching flyer that highlights earning potential from referrals for water damage restoration. Use high-contrast colors like blue, yellow, and white, with bold fonts and dynamic layouts. Include images of restoration work, cash, and happy clients. Emphasize key benefits like $500 minimum payouts, fast payments, and unlimited income potential. Keep instructions simple: refer a client, we handle the work, you get paid. Add a clear call-to-action and display contact details prominently. Focus on professionalism and energy.

Target Market(s)

Plumbers and Contractor 8.5" x11" Layout should be landscape not portrait.

Industry/Entity Type

General Contractor

Colors
0054AA
0677BA
7BADD7
CADEEF
E8F1F8
EB3D1F
EC4F4E
F09395
F8D3D4
FCEDEE

Requirements
Must have
• 8.5" x11" Layout should be landscape not portrait.
Nice to have

```html
<!DOCTYPE html>
<html lang="en">
<head>
<meta charset="utf-8">
<title>Refer a Flood – Partner Referral Flyer</title>
<link rel="stylesheet" href="https://fonts.googleapis.com/css2?family=Anton&family=Montserrat:wght@400;500;600;700;800&family=Oswald:wght@300;500&display=swap">
<style>
:root{
  --stage:#6b737d;
  --ink:#151517;
  --white:#ffffff;
  --blue:#0677ba;
  --blue-deep:#0054aa;
  --blue-soft:#5a86c9;
  --blue-light:#7badd7;
  --grey-text:#4a4d52;
  --card-shadow:0 4px 10px rgba(0,0,0,.35);
}
*{box-sizing:border-box;margin:0;padding:0}
html,body{width:1200px;height:1200px;overflow:hidden}
body{background:var(--stage);font-family:"Montserrat",sans-serif;position:relative}
.card{position:absolute;left:283px;width:635px;height:494px;overflow:hidden;box-shadow:var(--card-shadow);background:var(--white)}
.card--front{top:89px}
.card--back{top:627px;background:var(--ink)}
.card-art{position:absolute;inset:0;width:635px;height:494px}
.abs{position:absolute}

/* front */
.offer{left:29px;top:320px;width:308px;height:105px;border-radius:6px;background:var(--ink);overflow:hidden}
.offer-top{position:absolute;left:0;top:0;width:100%;height:78px;background:linear-gradient(90deg,var(--blue-soft),var(--blue))}
.offer-dash{position:absolute;inset:3px;border:1px dashed var(--white);border-radius:4px}
.offer-split{position:absolute;left:152px;top:0;width:2px;height:100%;background:var(--white)}
.offer-amount{position:absolute;top:0;height:78px;display:flex;align-items:center;justify-content:center;font-family:"Oswald",sans-serif;font-weight:500;color:var(--white);font-size:66px;line-height:1;letter-spacing:-2px}
.offer-amount sup{font-size:26px;align-self:flex-start;margin-top:10px;margin-right:2px}
.offer-amount--min{left:6px;width:130px}
.offer-amount--pct{left:166px;width:134px}
.offer-or{position:absolute;left:142px;top:34px;width:22px;height:22px;background:var(--white);border-radius:4px;font-weight:800;font-size:11px;color:var(--ink);display:flex;align-items:center;justify-content:center}
.offer-label{position:absolute;top:78px;height:27px;display:flex;align-items:center;justify-content:center;color:var(--white);font-weight:800;font-size:14px}
.offer-label--min{left:0;width:152px}
.offer-label--per{left:154px;width:154px}
.front-tagline{left:28px;top:458px;font-size:12.4px;color:var(--white);font-weight:500}
.brand-name{color:var(--white);font-family:"Montserrat",sans-serif;font-weight:500;letter-spacing:1.5px;text-align:center;white-space:nowrap}
.brand-name--front{left:397px;width:238px;top:100px;font-size:13px}
.why-title{left:357px;top:147px;width:278px;height:25px;color:var(--white);font-weight:700;font-size:17px;display:flex;align-items:center;justify-content:center;padding-left:24px}
.benefit{left:409px;width:198px;height:46px;border:1px solid rgba(255,255,255,.85);border-radius:3px;color:var(--white);font-size:10.3px;line-height:1.3;text-align:center;padding-top:13px}
.benefit-tag{position:absolute;top:-8px;left:50%;transform:translateX(-50%);background:var(--blue-soft);color:var(--white);font-weight:700;font-size:12px;padding:1px 7px;border-radius:10px;white-space:nowrap;box-shadow:0 0 0 4px var(--ink)}
.steps-row{left:397px;width:238px;top:442px;display:flex;justify-content:center;color:var(--white);font-weight:700;font-size:13.5px;line-height:1.25;text-align:center}
.steps-row span{padding:0 9px}
.steps-row span+span{border-left:1px solid var(--white)}

/* back */
.step{left:29px;width:322px;border:1.5px solid var(--ink);border-radius:4px;background:var(--white);overflow:hidden}
.step-num{position:absolute;left:0;top:0;bottom:0;width:30px;background:var(--ink);color:var(--white);font-weight:700;font-size:27px;display:flex;align-items:center;justify-content:center}
.step-head{margin-left:30px;height:27px;background:linear-gradient(90deg,var(--blue),var(--blue-soft));color:var(--white);font-weight:700;font-size:13px;letter-spacing:-.15px;white-space:nowrap;display:flex;align-items:center;padding-left:8px}
.step-body{margin-left:30px;padding:5px 8px 0;color:var(--grey-text);font-size:12px;line-height:1.25}
.cta{left:37px;top:428px;color:var(--white);font-weight:800;font-size:19.5px;line-height:1.1}
.phone-line{left:228px;top:428px;display:flex;align-items:center;gap:7px;color:var(--white);font-weight:800;font-size:33px;line-height:1}
.web-line{left:233px;top:461px;display:flex;align-items:center;gap:9px;color:var(--white);font-size:14.5px;font-weight:500}
.brand-name--back{left:495px;width:130px;top:463px;font-size:8.5px;letter-spacing:1px}
</style>
</head>
<body>

<section class="card card--front" aria-label="Flyer front">
  <svg class="card-art" viewBox="0 0 635 494">
    <defs>
      <linearGradient id="fBlue" x1="0" x2="1"><stop offset="0" stop-color="#0a6db8"/><stop offset="1" stop-color="#5a86c9"/></linearGradient>
      <linearGradient id="fPhoto" x1="0" y1="0" x2="0" y2="1"><stop offset="0" stop-color="#b9bcc0"/><stop offset=".5" stop-color="#d7d6d2"/><stop offset="1" stop-color="#5c5e63"/></linearGradient>
      <linearGradient id="fHead" x1="0" x2="1"><stop offset="0" stop-color="#5a86c9"/><stop offset="1" stop-color="#3f76c2"/></linearGradient>
    </defs>
    <path d="M0 0H400L372 116Q200 166 0 112Z" fill="url(#fPhoto)" role="img" aria-label="Photo of a flooded home interior with water rising over a staircase"/>
    <path d="M0 112Q200 166 372 116L368 128Q200 184 0 124Z" fill="var(--ink)"/>
    <path d="M0 448H420L392 494H0Z" fill="url(#fBlue)"/>
    <path d="M397 0H635V494H392Q330 250 397 0Z" fill="var(--ink)"/>
    <path d="M388 0Q321 250 384 494" fill="none" stroke="var(--blue)" stroke-width="4"/>
    <path d="M357 147H635V172H352Z" fill="url(#fBlue)"/>
    <text x="35" y="208" font-family="Oswald" font-weight="300" font-size="40" fill="var(--ink)" textLength="291" lengthAdjust="spacingAndGlyphs">EARN UNLIMITED CASH</text>
    <text x="35" y="262" font-family="Anton" font-size="56" fill="url(#fHead)" textLength="296" lengthAdjust="spacingAndGlyphs">GET PAID TO</text>
    <text x="35" y="306" font-family="Anton" font-size="42" fill="var(--ink)" textLength="293" lengthAdjust="spacingAndGlyphs">REFER A FLOOD</text>
  </svg>

  <div class="abs offer">
    <div class="offer-top"></div>
    <div class="offer-dash"></div>
    <div class="offer-split"></div>
    <div class="offer-amount offer-amount--min"><sup>$</sup>500</div>
    <div class="offer-amount offer-amount--pct">10%</div>
    <div class="offer-or">OR</div>
    <div class="offer-label offer-label--min">Minimum</div>
    <div class="offer-label offer-label--per">Per Referral!</div>
  </div>

  <p class="abs front-tagline">Partner with the #1 Water Damage Restoration Team</p>

  <p class="abs brand-name brand-name--front">HARBOR CREST REMODEL</p>
  <h2 class="abs why-title">Why Partner with Us?</h2>

  <div class="abs benefit" style="top:194px"><span class="benefit-tag">Guaranteed Payout</span>Minimum $500 or<br>10% of the invoice, paid fast.</div>
  <div class="abs benefit" style="top:255px"><span class="benefit-tag">Free Evaluations</span>We assess damage and process<br>insurance claims for your clients.</div>
  <div class="abs benefit" style="top:315px"><span class="benefit-tag">Industry Leaders</span>Certified experts with 24/7<br>rapid response.</div>
  <div class="abs benefit" style="top:376px"><span class="benefit-tag">Affordable Solutions</span>Lowest out-of-pocket costs<br>for your customers.</div>

  <div class="abs steps-row"><span>Send<br>Referrals</span><span>Get<br>Paid</span><span>Grow Your<br>Business</span></div>
</section>

<section class="card card--back" aria-label="Flyer back">
  <svg class="card-art" viewBox="0 0 635 494">
    <defs>
      <linearGradient id="bBlue" x1="0" x2="1"><stop offset="0" stop-color="#0a6db8"/><stop offset="1" stop-color="#5a86c9"/></linearGradient>
      <linearGradient id="bPhoto" x1="0" y1="0" x2="1" y2="1"><stop offset="0" stop-color="#bcd6e8"/><stop offset=".5" stop-color="#eef0f1"/><stop offset="1" stop-color="#c9ccce"/></linearGradient>
    </defs>
    <rect width="635" height="494" fill="var(--ink)"/>
    <path d="M2 166H375Q356 300 412 414H2Z" fill="var(--white)"/>
    <path d="M424 0H635V414H424Q330 220 424 0Z" fill="url(#bPhoto)" role="img" aria-label="Photo of a bright, newly remodeled open-plan living room with a grey sofa and tall windows"/>
    <path d="M418 0Q324 220 418 414" fill="none" stroke="var(--blue)" stroke-width="4"/>
    <path d="M0 414H220Q214 455 222 494H0Z" fill="url(#bBlue)"/>
    <text x="35" y="88" font-family="Oswald" font-weight="300" font-size="76" fill="var(--white)" textLength="317" lengthAdjust="spacingAndGlyphs">GET PAID TO</text>
    <text x="35" y="142" font-family="Anton" font-size="50" fill="var(--white)" textLength="318" lengthAdjust="spacingAndGlyphs">REFER A FLOOD</text>
  </svg>

  <div class="abs step" style="top:186px;height:56px"><div class="step-num">1</div><div class="step-head">Refer Flood, Water and Mold Damage</div><div class="step-body">Call, book online, or text us directly.</div></div>
  <div class="abs step" style="top:251px;height:67px"><div class="step-num">2</div><div class="step-head">We Take Care of Everything</div><div class="step-body">Free evaluations, insurance claims, and<br>professional service.</div></div>
  <div class="abs step" style="top:327px;height:67px"><div class="step-num">3</div><div class="step-head">Get Paid Fast</div><div class="step-body">$500 minimum or 10% of the invoice within<br>48 hours of final payment.</div></div>

  <p class="abs cta">CALL TEXT OR<br>BOOK ON-LINE</p>

  <div class="abs phone-line">
    <svg width="22" height="22" viewBox="0 0 22 22" aria-hidden="true"><circle cx="11" cy="11" r="11" fill="var(--blue-soft)"/><path d="M7.2 5.5l2.2 2.6-1.2 1.5c.8 1.7 2 2.9 3.6 3.7l1.5-1.2 2.6 2.2-1.3 1.9c-4.6-.5-8.7-4.5-9.2-9.1z" fill="var(--white)"/></svg>
    555-014-2290
  </div>
  <div class="abs web-line">
    <svg width="14" height="14" viewBox="0 0 14 14" aria-hidden="true" fill="none" stroke="var(--blue-light)" stroke-width="1"><circle cx="7" cy="7" r="6"/><ellipse cx="7" cy="7" rx="2.6" ry="6"/><path d="M1 7h12M2 3.8h10M2 10.2h10"/></svg>
    HarborCrestRemodel.com
  </div>
  <p class="abs brand-name brand-name--back">HARBOR CREST REMODEL</p>
</section>

</body>
</html>
```